A website for a Maltese Law Firm

Our law firm needs a website to further its business. The site should have a simple yet effective design. We would need the following sections: About us, Practice Areas, About Malta, Contact. These should be further split as follows:

About us: Our firm, Our values, What others say, Offices

Practice Areas: Crimimal, Citizenship & Residence, Overseas Patron Scheme, Criminal Defence, Civil Litigation, Arbitration and ADR, Commercial and Corporate, Media Law.

About Malta: just one section.

Contact: Just one section

We would also need a news feed at the front of the site to include latest news regarding our cases.

At the bottom we need a section for our Terms and a Privacy Statement.

Our logo is being attached.

Target Market(s)

All clients looking for legal assistance in Malta

Industry/Entity Type

Legal

Coding

Coded - Design and coding required

Number of Pages Required

1 page

Requirements
Must have
• It must be simple yet striking.

```html
<!DOCTYPE html>
<html lang="en">
<head>
<meta charset="utf-8">
<title>Brevane &amp; Sollari Advocates</title>
<link href="https://fonts.googleapis.com/css2?family=Open+Sans:wght@400;600;700&family=Roboto+Slab:wght@400;700&display=swap" rel="stylesheet">
<style>
:root{
  --crimson:#a3214b;
  --orange:#ef5a2a;
  --ink:#1f1f1f;
  --text:#3a3a3a;
  --muted:#8a8a8a;
  --grey-band:#ececec;
  --grey-light:#f5f5f5;
  --button:#8c8c8c;
  --white:#ffffff;
}
*{margin:0;padding:0;box-sizing:border-box}
html,body{width:1200px;height:4972px;overflow:hidden;background:var(--white)}
body{position:relative;font-family:"Open Sans",Arial,sans-serif;color:var(--text);font-size:14px;line-height:1.55}
.abs{position:absolute}
.slab{font-family:"Roboto Slab",Georgia,serif}
.section-title{position:absolute;left:0;width:1200px;text-align:center;font-family:"Roboto Slab",Georgia,serif;font-weight:700;font-size:30px;letter-spacing:1px;color:var(--ink);text-transform:uppercase}
.section-title span{color:var(--crimson)}
.section-title::after{content:"";display:block;width:70px;height:3px;background:var(--crimson);margin:6px auto 0}
p{margin-bottom:14px}

/* header */
.top-strip{left:0;top:0;width:1200px;height:16px;background:var(--crimson)}
.brand{left:40px;top:76px;font-family:"Roboto Slab",Georgia,serif;font-weight:700;font-size:19px;color:var(--ink);letter-spacing:.5px;text-transform:uppercase}
.brand-small{font-size:14px}
.nav{right:50px;top:82px;display:flex;gap:38px;font-size:14px;font-weight:700;color:var(--crimson);text-transform:uppercase}
.hero{left:0;top:133px;width:1200px;height:530px;background:linear-gradient(100deg,#c98b6e 0%,#8e5a6a 35%,#b98a8a 60%,#efe0d8 100%)}

/* news */
.news-card{position:absolute;top:762px;width:352px}
.news-photo{width:352px;height:298px;background:linear-gradient(135deg,#3c4a5e,#9aa6b4 60%,#d9dde2)}
.news-title{margin-top:18px;font-weight:700;font-size:16px;color:var(--ink)}
.news-text{margin-top:12px;font-size:13px;line-height:1.6}
.news-meta{margin-top:16px;border-top:1px solid #cfcfcf;padding-top:10px;display:flex;justify-content:space-between;font-size:12px;color:var(--ink)}

/* firm */
.kicker{left:40px;top:1450px;font-family:"Roboto Slab",Georgia,serif;font-size:28px;color:#9b9b9b;text-transform:uppercase;letter-spacing:1px}
.intro-heading{left:40px;top:1490px;font-family:"Roboto Slab",Georgia,serif;font-weight:700;font-size:56px;color:var(--orange);letter-spacing:1px}
.intro-text{left:40px;top:1560px;width:600px;font-size:15px}
.portrait{left:663px;top:1360px;width:430px;height:563px;background:linear-gradient(180deg,#f4f4f4 0%,#d9c6b4 35%,#3a3a3e 70%,#2a2a2e 100%)}

/* value */
.value-band{left:0;top:1923px;width:1200px;height:381px;background:var(--grey-light)}
.value-photo{left:0;top:1923px;width:607px;height:381px;background:linear-gradient(120deg,#d6cbb8,#b9826c 45%,#e8e0d6)}
.value-heading{left:676px;top:1980px;font-family:"Roboto Slab",Georgia,serif;font-weight:700;font-size:38px;color:var(--ink)}
.value-heading span{color:var(--crimson)}
.value-heading::after{content:"";display:block;width:160px;height:3px;background:var(--crimson);margin-top:2px}
.value-text{left:676px;top:2040px;width:490px;font-size:14px}

/* testimonial */
.quote{left:150px;top:2405px;width:900px;text-align:center;font-size:14px}
.avatar{left:578px;top:2500px;width:44px;height:44px;border-radius:50%;background:linear-gradient(#d8c4b2,#9c8b7e)}
.quote-name{left:0;top:2556px;width:1200px;text-align:center;font-size:14px;color:var(--ink);text-transform:uppercase}
.quote-role{left:0;top:2578px;width:1200px;text-align:center;font-size:11px;font-weight:700;color:var(--crimson);text-transform:uppercase}
.arrow{top:2370px}

/* offices */
.offices-band{left:0;top:2652px;width:1200px;height:391px;background:var(--grey-band)}
.offices-photo{left:0;top:2652px;width:603px;height:391px;background:linear-gradient(160deg,#6d6d6d,#3b3b3b 55%,#8c8c8c)}
.offices-heading{left:646px;top:2680px;font-family:"Roboto Slab",Georgia,serif;font-weight:700;font-size:40px;color:var(--crimson)}
.offices-heading::after{content:"";display:block;width:160px;height:3px;background:var(--crimson);margin-top:0}
.office{top:2745px;width:270px;font-size:14px;color:var(--ink);line-height:1.5}

/* practice */
.practice-band{left:0;top:3043px;width:1200px;height:850px;background:repeating-linear-gradient(180deg,#fafafa 0 6px,#f1f1f1 6px 8px)}
.practice-kicker{left:0;top:3080px;width:1200px;text-align:center;font-size:15px;font-weight:600;color:var(--ink);text-transform:uppercase;letter-spacing:1px}
.practice-heading{left:0;top:3104px;width:1200px;text-align:center;font-family:"Roboto Slab",Georgia,serif;font-weight:700;font-size:40px;color:var(--crimson)}
.area{position:absolute;width:250px;text-align:center}
.area svg{display:block;margin:0 auto}
.area h3{margin-top:12px;font-family:"Roboto Slab",Georgia,serif;font-size:17px;font-weight:700;color:var(--crimson);text-transform:uppercase;white-space:nowrap}
.area p{margin:14px 0 0;text-align:left;font-size:13px;line-height:1.6;color:var(--ink)}
.area .btn{display:inline-block;margin-top:28px;width:150px;height:30px;line-height:30px;background:var(--button);color:var(--white);font-size:11px;font-weight:700;text-transform:uppercase}

/* malta */
.malta-band{left:0;top:4034px;width:1200px;height:375px;background:linear-gradient(90deg,#efefef 0%,#e6e6e6 50%,#d6dbe4 100%)}
.malta-skyline{left:620px;top:4034px;width:580px;height:375px;background:linear-gradient(180deg,#e6e9f0 0%,#c3cbd9 60%,#a6b0c2 100%)}
.malta-text{left:60px;top:4130px;width:570px;font-size:15px;color:var(--ink)}

/* contact */
.form-panel{left:620px;top:4498px;width:580px;height:474px;background:var(--orange);clip-path:polygon(14% 0,100% 0,100% 100%,0 100%)}
.form-title{left:790px;top:4525px;width:410px;text-align:center;font-family:"Roboto Slab",Georgia,serif;font-size:30px;font-weight:700;color:var(--white);text-transform:uppercase}
.form-label{left:770px;font-weight:700;font-size:16px;color:var(--white)}
.form-field{left:845px;width:320px;height:36px;background:var(--white);border-radius:2px;font-size:13px;color:#b5b5b5;padding:8px 10px}
.form-submit{left:845px;top:4850px;width:140px;height:36px;background:var(--crimson);color:var(--white);font-weight:700;font-size:15px;text-align:center;line-height:36px;text-transform:uppercase}
.footer-col{top:4620px;font-size:14px;color:var(--ink);line-height:1.45}
.footer-col b{font-size:13px;text-transform:uppercase}
.terms{left:40px;top:4870px;font-size:12px;font-weight:700;color:var(--crimson);text-transform:uppercase}
.copyright{left:0;top:4923px;width:1200px;height:49px;background:#dcdcdc;padding:14px 40px;font-size:12px;color:var(--text)}
</style>
</head>
<body>

<!-- header -->
<div class="abs top-strip"></div>
<div class="abs brand">Brevane &amp; Sollari <span class="brand-small">Advocates</span></div>
<nav class="abs nav"><span>About us</span><span>Practice areas</span><span>About Malta</span><span>Contact</span></nav>
<div class="abs hero" role="img" aria-label="Courtroom interior with a brass scale of justice in the foreground"></div>

<!-- latest news -->
<h2 class="section-title" style="top:685px">Latest <span>News</span></h2>
<article class="news-card" style="left:139px">
  <div class="news-photo" role="img" aria-label="Business people shaking hands in an office"></div>
  <div class="news-title">Lorem ipsum dolor sit amet</div>
  <div class="news-text">Lorem ipsum dolor sit amet, consectetur adipiscing elit. Graece donan, latine voluptatem vocant. Nos paulo ad haec additis finem faciamus aliquando. Mihi enim satis est, ipsis non satis. Si enim ita est, vide ne facinus facias, cum mori suadeas.</div>
  <div class="news-meta"><span>June 12, 2016</span><span>Continue &gt;&gt;</span></div>
</article>
<article class="news-card" style="left:709px">
  <div class="news-photo" role="img" aria-label="Close view of two people shaking hands across a desk"></div>
  <div class="news-title">Lorem ipsum dolor sit amet</div>
  <div class="news-text">Lorem ipsum dolor sit amet, consectetur adipiscing elit. Graece donan, latine voluptatem vocant. Nos paulo ad haec additis finem faciamus aliquando. Mihi enim satis est, ipsis non satis. Si enim ita est, vide ne facinus facias, cum mori suadeas.</div>
  <div class="news-meta"><span>June 12, 2016</span><span>Continue &gt;&gt;</span></div>
</article>

<!-- our firm -->
<h2 class="section-title" style="top:1312px">Our <span>Firm</span></h2>
<div class="abs kicker">All about Brevane and Sollari</div>
<div class="abs intro-heading">INTRODUCTION</div>
<div class="abs intro-text">
  <p>Lorem ipsum dolor sit amet, consectetur adipiscing elit. Et quod est munus, quod opus sapientiae? Et nemo nimium beatus est; Est, ut dicis, inquam. Ut non sine causa ex iis memoriae ducta sit disciplina. Duo Reges: constructio interrete. Stuprata per vim Lucretia a regis filio testata civis se ipsa interemit. Et ais, si una littera commota sit, fore tota ut labet disciplina. Torquatus, is qui consul cum Cn.</p>
  <p>Quos quidem tibi studiose et diligenter tractandos magnopere censeo. Septem autem illi non suo, sed populorum suffragio omnium nominati sunt. Nihil enim hoc differt. Omnes enim iucundum motum, quo sensus hilaretur.</p>
</div>
<div class="abs portrait" role="img" aria-label="Portrait of a lawyer in a dark suit"></div>

<!-- our value -->
<div class="abs value-band"></div>
<div class="abs value-photo" role="img" aria-label="Lawyer working at a desk in a bright office"></div>
<div class="abs value-heading">OUR <span>VALUE</span></div>
<div class="abs value-text">
  <p>Lorem ipsum dolor sit amet, consectetur adipiscing elit. Et quod est munus, quod opus sapientiae? Et nemo nimium beatus est; Est, ut dicis, inquam. Ut non sine causa ex iis memoriae ducta sit disciplina. Duo Reges: constructio interrete. Stuprata per vim Lucretia a regis filio testata civis se ipsa interemit. Et ais, si una littera commota sit, fore tota ut labet disciplina. Torquatus, is qui consul cum Cn.</p>
  <p>Quos quidem tibi studiose et diligenter tractandos magnopere censeo. Septem autem illi non suo, sed populorum suffragio omnium nominati sunt. Nihil enim hoc differt. Omnes enim iucundum motum, quo sensus hilaretur.</p>
</div>

<!-- testimonials -->
<h2 class="section-title" style="top:2335px;color:var(--crimson)">What others say</h2>
<svg class="abs arrow" style="left:28px" width="20" height="34" viewBox="0 0 20 34"><path d="M16 3 3 17l13 14" fill="none" stroke="#111" stroke-width="4"/></svg>
<svg class="abs arrow" style="left:1130px" width="20" height="34" viewBox="0 0 20 34"><path d="M4 3l13 14L4 31" fill="none" stroke="#111" stroke-width="4"/></svg>
<div class="abs quote">Suspendisse commodo auctor molestie. Mauris accumsan massa consequat pharetra. Suspendisse dapibus erat lectus rutrum bibendum. Praesent scelerisque. Fusce vel enim sapien. Vivamus pellentesque hendrerit erat, sit amet dictum nibh viverra iaculis. Sed porta nisl molestie hendrerit. Integer tempus pulvinar laoreet.</div>
<div class="abs avatar" role="img" aria-label="Client portrait"></div>
<div class="abs quote-name">Marina Delcour</div>
<div class="abs quote-role">Corporate lawyer</div>

<!-- offices -->
<div class="abs offices-band"></div>
<div class="abs offices-photo" role="img" aria-label="City skyline at dusk seen from above"></div>
<div class="abs offices-heading">OFFICES</div>
<div class="abs office" style="left:646px">Address:<br>12 Harbour Lane, Suite 4,<br>Valletta VLT 1020,<br>Malta<br><br>Phone:<br>+356 2100 0000 - Office<br>+356 2100 0001 - Fax<br>office@brevanesollari.example</div>
<div class="abs office" style="left:938px">Address:<br>12 Harbour Lane, Suite 4,<br>Valletta VLT 1020,<br>Malta<br><br>Phone:<br>+356 2100 0000 - Office<br>+356 2100 0001 - Fax<br>office@brevanesollari.example</div>

<!-- practice areas -->
<div class="abs practice-band"></div>
<div class="abs practice-kicker">This is what we are good at</div>
<div class="abs practice-heading">PRACTICE AREAS</div>

<div class="area" style="left:41px;top:3195px">
  <svg width="90" height="90" viewBox="0 0 90 90"><circle cx="45" cy="45" r="42" fill="#fff" stroke="#ef5a2a" stroke-width="3"/><circle cx="33" cy="50" r="11" fill="none" stroke="#ef5a2a" stroke-width="4"/><circle cx="57" cy="50" r="11" fill="none" stroke="#ef5a2a" stroke-width="4"/><path d="M40 40h10" stroke="#ef5a2a" stroke-width="4"/></svg>
  <h3>Criminal</h3>
  <p>Lorem ipsum dolor sit amet, consectetur adipiscing elit. Et quod est munus, quod opus sapientiae? Et nemo nimium beatus est; Est, ut dicis, inquam. Ut non sine causa ex iis memoriae ducta sit disciplina.</p>
  <span class="btn">Continue</span>
</div>
<div class="area" style="left:306px;top:3195px">
  <svg width="90" height="90" viewBox="0 0 90 90"><circle cx="45" cy="45" r="42" fill="#fff" stroke="#ef5a2a" stroke-width="3"/><rect x="30" y="24" width="30" height="40" fill="#ef5a2a"/><path d="M36 34h18M36 42h18M36 50h12" stroke="#fff" stroke-width="3"/></svg>
  <h3>Citizenship &amp; Residence</h3>
  <p>Lorem ipsum dolor sit amet, consectetur adipiscing elit. Et quod est munus, quod opus sapientiae? Et nemo nimium beatus est; Est, ut dicis, inquam. Ut non sine causa ex iis memoriae ducta sit disciplina.</p>
  <span class="btn">Continue</span>
</div>
<div class="area" style="left:611px;top:3195px">
  <svg width="90" height="90" viewBox="0 0 90 90"><circle cx="45" cy="45" r="42" fill="#fff" stroke="#ef5a2a" stroke-width="3"/><circle cx="45" cy="34" r="10" fill="#ef5a2a"/><path d="M27 66c0-12 8-19 18-19s18 7 18 19z" fill="#ef5a2a"/></svg>
  <h3>Overseas Patron Scheme</h3>
  <p>Lorem ipsum dolor sit amet, consectetur adipiscing elit. Et quod est munus, quod opus sapientiae? Et nemo nimium beatus est; Est, ut dicis, inquam. Ut non sine causa ex iis memoriae ducta sit disciplina.</p>
  <span class="btn">Continue</span>
</div>
<div class="area" style="left:913px;top:3195px">
  <svg width="90" height="90" viewBox="0 0 90 90"><circle cx="45" cy="45" r="42" fill="#fff" stroke="#ef5a2a" stroke-width="3"/><path d="M45 22v44M25 30h40M34 66h22" stroke="#ef5a2a" stroke-width="4"/><path d="M25 30l-8 18h16zM65 30l-8 18h16z" fill="#ef5a2a"/></svg>
  <h3>Criminal Defence</h3>
  <p>Lorem ipsum dolor sit amet, consectetur adipiscing elit. Et quod est munus, quod opus sapientiae? Et nemo nimium beatus est; Est, ut dicis, inquam. Ut non sine causa ex iis memoriae ducta sit disciplina.</p>
  <span class="btn">Continue</span>
</div>

<div class="area" style="left:41px;top:3560px">
  <svg width="90" height="90" viewBox="0 0 90 90"><circle cx="45" cy="45" r="42" fill="#fff" stroke="#ef5a2a" stroke-width="3"/><rect x="34" y="22" width="24" height="14" transform="rotate(-45 46 29)" fill="#ef5a2a"/><path d="M42 38 26 58" stroke="#ef5a2a" stroke-width="6"/><rect x="46" y="60" width="22" height="6" fill="#ef5a2a"/></svg>
  <h3>Civil Litigation</h3>
  <p>Lorem ipsum dolor sit amet, consectetur adipiscing elit. Et quod est munus, quod opus sapientiae? Et nemo nimium beatus est; Est, ut dicis, inquam. Ut non sine causa ex iis memoriae ducta sit disciplina.</p>
  <span class="btn">Continue</span>
</div>
<div class="area" style="left:306px;top:3560px">
  <svg width="90" height="90" viewBox="0 0 90 90"><circle cx="45" cy="45" r="42" fill="#fff" stroke="#ef5a2a" stroke-width="3"/><path d="M18 40l14-8 13 8 13-8 14 8-14 14H32z" fill="#ef5a2a"/></svg>
  <h3>Arbitration and ADR</h3>
  <p>Lorem ipsum dolor sit amet, consectetur adipiscing elit. Et quod est munus, quod opus sapientiae? Et nemo nimium beatus est; Est, ut dicis, inquam. Ut non sine causa ex iis memoriae ducta sit disciplina.</p>
  <span class="btn">Continue</span>
</div>
<div class="area" style="left:611px;top:3560px">
  <svg width="90" height="90" viewBox="0 0 90 90"><circle cx="45" cy="45" r="42" fill="#fff" stroke="#ef5a2a" stroke-width="3"/><rect x="30" y="24" width="30" height="42" fill="#ef5a2a"/><path d="M38 24v42M45 24v42M52 24v42" stroke="#fff" stroke-width="2"/></svg>
  <h3>Commercial &amp; Corporate</h3>
  <p>Lorem ipsum dolor sit amet, consectetur adipiscing elit. Et quod est munus, quod opus sapientiae? Et nemo nimium beatus est; Est, ut dicis, inquam. Ut non sine causa ex iis memoriae ducta sit disciplina.</p>
  <span class="btn">Continue</span>
</div>
<div class="area" style="left:913px;top:3560px">
  <svg width="90" height="90" viewBox="0 0 90 90"><circle cx="45" cy="45" r="42" fill="#fff" stroke="#ef5a2a" stroke-width="3"/><rect x="24" y="34" width="42" height="30" rx="3" fill="none" stroke="#ef5a2a" stroke-width="4"/><path d="M36 24l9 10 9-10" fill="none" stroke="#ef5a2a" stroke-width="3"/></svg>
  <h3>Media Law</h3>
  <p>Lorem ipsum dolor sit amet, consectetur adipiscing elit. Et quod est munus, quod opus sapientiae? Et nemo nimium beatus est; Est, ut dicis, inquam. Ut non sine causa ex iis memoriae ducta sit disciplina.</p>
  <span class="btn">Continue</span>
</div>

<!-- about malta -->
<h2 class="section-title" style="top:3935px">About <span>Malta</span></h2>
<div class="abs malta-band"></div>
<div class="abs malta-skyline" role="img" aria-label="Faded city skyline in pale blue tones"></div>
<div class="abs malta-text">Lorem ipsum dolor sit amet, consectetur adipiscing elit. Et quod est munus, quod opus sapientiae? Et nemo nimium beatus est; Est, ut dicis, inquam. Ut non sine causa ex iis memoriae ducta sit disciplina. Duo Reges: constructio interrete. Stuprata per vim Lucretia a regis filio testata civis se ipsa interemit. Et ais, si una littera commota sit, fore tota ut labet disciplina. Torquatus, is qui consul cum Cn.</div>

<!-- contact -->
<h2 class="section-title" style="top:4440px;color:var(--orange)">Contact us</h2>
<div class="abs form-panel"></div>
<div class="abs form-title">Consulting form</div>
<div class="abs form-label" style="top:4597px">Name:</div>
<div class="abs form-field" style="top:4590px">Your Name</div>
<div class="abs form-label" style="top:4649px">Email:</div>
<div class="abs form-field" style="top:4642px">Email</div>
<div class="abs form-label" style="top:4701px">Message:</div>
<div class="abs form-field" style="top:4694px;height:140px">Your Message</div>
<div class="abs form-submit">Submit</div>

<div class="abs brand" style="top:4528px;font-size:17px">Brevane &amp; Sollari <span class="brand-small">Advocates</span></div>
<div class="abs footer-col" style="left:40px"><b>Address:</b><br>12 Harbour Lane, Suite 4,<br>Valletta VLT 1020,<br>Malta<br><br>Phone:<br>+356 2100 0000 - Office<br>+356 2100 0001 - Fax<br>office@brevanesollari.example</div>
<div class="abs footer-col" style="left:288px"><b>About us</b><br>Our Firm<br>Our Values<br>What Others Say<br>Offices</div>
<div class="abs footer-col" style="left:431px"><b>Practice areas</b><br>Criminal<br>Citizenship &amp; Residence<br>Overseas Patron Scheme<br>Criminal Defence<br>Arbitration and ADR<br>Commercial and Corporate<br>Media Law</div>
<div class="abs terms">Terms and privacy statement</div>
<div class="abs copyright">Copyright &copy; 2016. Brevane &amp; Sollari Advocates</div>

</body>
</html>
```